Anzeigengestaltung für Steuerberater, Unternehmensberater
Zielgruppe
Steuerberater, Unternehmensberater, Business-Coach, VOLT-Coach
Aufgabenstellung
es ist für eine gedruckte Vereinszeitschrift
Größe 12,5 x 19 cm
Bitte nicht die vorhandenen Vorlage (Datei Lumigram) verwenden

```html
<!DOCTYPE html>
<html lang="de">
<head>
<meta charset="utf-8">
<title>Anzeige Steuerberatung</title>
<link rel="stylesheet" href="https://fonts.googleapis.com/css2?family=Jost:wght@300;400;500;600&display=swap">
<style>
  :root {
    --blue: #3a62a8;
    --blue-deep: #2f57a3;
    --green: #8cc13f;
    --ink: #3e3f4e;
    --white: #ffffff;
    --photo-light: #eeeef2;
    --photo-dark: #c8c8d0;
  }
  * { margin: 0; padding: 0; box-sizing: border-box; }
  html, body { width: 789px; height: 1200px; overflow: hidden; }
  body { font-family: "Jost", sans-serif; color: var(--ink); }
  .ad {
    position: relative; width: 789px; height: 1200px; overflow: hidden;
    background: var(--photo-light);
  }
  .ad__photo {
    position: absolute; inset: 0;
    background: linear-gradient(150deg, var(--photo-light) 0%, #e4e4ea 45%, var(--photo-dark) 100%);
  }
  .ad__arc { position: absolute; left: 0; top: 0; width: 789px; height: 530px; }
  .ad__icon {
    position: absolute; left: 556px; top: 96px; width: 260px; height: 376px;
    transform: rotate(8deg); transform-origin: top left;
    background: rgba(255,255,255,0.14); border-radius: 6px;
  }
  .headline {
    position: absolute; left: 50px; top: 82px;
    font-weight: 300; font-size: 84px; line-height: 82px; color: var(--white);
    letter-spacing: 0.5px;
  }
  .headline__accent {
    display: inline-block; margin-top: 2px;
    font-weight: 600; color: var(--green);
    padding-bottom: 4px; border-bottom: 7px solid var(--green);
  }
  .services {
    position: absolute; left: 50px; top: 556px; list-style: none;
    font-size: 34px; line-height: 53.5px; font-weight: 400; color: var(--ink);
  }
  .contact { position: absolute; left: 50px; top: 1014px; }
  .contact__title {
    font-size: 26px; font-weight: 500; letter-spacing: 2.6px; color: var(--green);
    margin-bottom: 8px;
  }
  .contact__line {
    display: inline-block; font-size: 25px; font-weight: 500; color: var(--blue-deep);
    border-bottom: 3px solid var(--blue-deep); line-height: 36px; margin-bottom: 8px;
  }
  .brands { position: absolute; left: 529px; top: 1012px; width: 197px; }
  .brand {
    display: flex; align-items: center; justify-content: center; gap: 8px;
    font-weight: 500; white-space: nowrap;
  }
  .brand--advisor { height: 42px; font-size: 21px; color: var(--blue-deep); letter-spacing: 0.5px; }
  .brand--company { margin-top: 24px; height: 44px; font-size: 24px; color: var(--ink); letter-spacing: 1px; }
  .brand__mark { width: 14px; height: 14px; background: var(--green); }
</style>
</head>
<body>
<main class="ad">
  <div class="ad__photo" role="img" aria-label="Hintergrundfoto: Hände an einem Laptop mit Smartwatch und Smartphone auf dem Schreibtisch"></div>

  <svg class="ad__arc" viewBox="0 0 789 530" aria-hidden="true">
    <path d="M0,0 H789 V374 C700,470 590,527 420,527 C240,527 100,470 0,396 Z" fill="var(--blue)" opacity="0.94"/>
  </svg>

  <div class="ad__icon" role="img" aria-label="Linien-Illustration: Dokument mit Dollarzeichen, Person und Sprechblase"></div>

  <h1 class="headline">
    Verbessern<br>
    Sie mit uns<br>
    <span class="headline__accent">Ihr Geschäft!</span>
  </h1>

  <ul class="services">
    <li>- Steuerberatung</li>
    <li>- Unternehmensberatung</li>
    <li>- Organisationsentwicklung</li>
    <li>- agile Arbeitsmethoden</li>
    <li>- Employer Branding</li>
    <li>- Business-Coaching</li>
    <li>- Change Mangagement</li>
  </ul>

  <section class="contact">
    <p class="contact__title">KONTAKTIEREN SIE UNS:</p>
    <span class="contact__line">Birkenweg 12, 51234 Talheim</span><br>
    <span class="contact__line">Tel +49 2201 5587210</span>
  </section>

  <div class="brands">
    <div class="brand brand--advisor">JONAS FALK</div>
    <div class="brand brand--company"><span class="brand__mark"></span>VERALO GMBH</div>
  </div>
</main>
</body>
</html>
```